Agency Website & Personal brand

My name is Nikolas Vourtelis & I've been a digital marketer & an e-commerce expert since 2010.

- I've spoken to 20 different events around the world up to 3,000 people in size.
- I've sold over 1500 training courses around e-commerce growth.
- I have over 100 testimonials (video & photo) from successful students who bought my training
- I have dozens of video testimonials from respected entrepreneurs that vouch for me and my work
- I have photos with marketing legends with that I shared the stage like Colin Marsh, Thomas Halvorenko, Brent Loy & more
- I am the host of the Aegean Roundtable since 2017 - a high-level networking event for 7 & 8 figure entrepreneurs - 100 people have come to Greece since 2017
- I have tons of videos created where I showcase my expertise on growth
- I have worked with dozens of e-commerce stores on their growth & helped them scale to multiple 6, 7 & 8 figures either on consulting

I need a website design that showcases my authority & be a lead generating machine.

The goal is to bring people on a call with me but also grab their email and start building the relationship with them and free valuable content

We have 3 offers :

1. Paid ads (Done for You)
2. Consulting/Mastermind (Done with You)
3. Training (Do it Yourself)

```html
<!DOCTYPE html>
<html lang="en">
<head>
<meta charset="utf-8">
<title>Nikolas Vourtelis — Public Speaker & eCom Trainer</title>
<link href="https://fonts.googleapis.com/css2?family=Poppins:wght@400;500;600;700;800&display=swap" rel="stylesheet">
<style>
:root{
  --red:#e3173d;
  --dark:#1b1b1d;
  --dark-2:#232325;
  --light:#f1f1f1;
  --ink:#1a1a1a;
  --body:#444;
  --white:#fff;
}
*{margin:0;padding:0;box-sizing:border-box}
html,body{width:1200px;height:4747px;overflow:hidden}
body{font-family:'Poppins',sans-serif;color:var(--ink);background:var(--white);position:relative}
.abs{position:absolute}
section{position:absolute;left:0;width:1200px;overflow:hidden}
.btn{position:absolute;background:var(--red);color:var(--white);font-weight:600;font-size:14px;text-transform:uppercase;display:flex;align-items:center;justify-content:center;letter-spacing:.2px;z-index:3}
.ph{position:absolute}

/* hero */
.hero{top:0;height:673px}
.hero-bg{left:0;top:0;width:1200px;height:673px;background:linear-gradient(100deg,#6d97d4 0%,#86a5dc 40%,#a7b3e2 70%,#d9dcef 100%)}
.hero-photo{left:540px;top:40px;width:420px;height:600px;background:radial-gradient(ellipse at 50% 45%,rgba(60,72,98,.55) 0%,rgba(80,95,130,.3) 45%,rgba(120,140,190,0) 72%)}
.brand{left:98px;top:22px;color:var(--white);font-size:28px;font-weight:400;z-index:2}
.nav{left:0;top:30px;color:var(--white);font-size:14px;z-index:2}
.nav a{position:absolute;white-space:nowrap;color:var(--white);text-decoration:none}
.nav-cta{left:958px;top:22px;width:142px;height:37px}
.hero-title{left:98px;top:168px;color:var(--white);font-size:51px;font-weight:600;line-height:50px;z-index:2}
.hero-sub{left:100px;top:336px;color:var(--white);font-size:22px;line-height:29px;width:420px;z-index:2}
.hero-book{left:100px;top:405px;color:var(--white);font-size:19px;z-index:2}
.hero-book u{text-underline-offset:3px}
.hero-input{left:100px;top:460px;width:401px;height:34px;background:var(--white);font-size:12px;color:#555;padding:9px 13px;z-index:2}
.hero-btn{left:100px;top:507px;width:401px;height:37px}

/* about */
.about{top:673px;height:525px}
.video-frame{left:120px;top:79px;width:485px;height:369px;background:var(--white);box-shadow:0 4px 18px rgba(0,0,0,.25);padding:9px}
.video-fill{width:100%;height:100%;background:linear-gradient(160deg,#c9ccd2 0%,#9aa0aa 40%,#5b5f68 100%)}
.play-red{width:66px;height:66px;border-radius:50%;background:var(--red);display:flex;align-items:center;justify-content:center}
.about-title{left:665px;top:94px;font-size:34px;font-weight:600}
.about-text{left:665px;top:143px;width:430px;font-size:15px;line-height:30.5px;color:var(--body)}
.about-btn{left:665px;top:389px;width:142px;height:36px}

/* story */
.story{top:1198px;height:673px;background:var(--dark)}
.ghost{color:rgba(255,255,255,.06);font-weight:800;text-transform:uppercase;white-space:nowrap}
.story-ghost{left:92px;top:72px;font-size:90px}
.story-title{left:98px;top:142px;color:var(--white);font-size:33px;font-weight:600}
.story-list{left:98px;top:208px;width:470px;list-style:none;color:var(--white);font-size:15px;line-height:21px}
.story-list li{position:relative;padding-left:20px;margin-bottom:13px}
.story-list li::before{content:"";position:absolute;left:0;top:4px;width:13px;height:13px;border:2px solid var(--white);border-radius:50%;box-sizing:border-box}
.story-list li::after{content:"";position:absolute;left:4px;top:8px;width:5px;height:5px;background:var(--white);border-radius:50%}
.story-btn{left:100px;top:512px;width:142px;height:35px}
.story-photo{left:640px;top:40px;width:520px;height:600px;background:radial-gradient(ellipse at 55% 60%,rgba(72,90,128,.55) 0%,rgba(50,60,85,.35) 40%,rgba(27,27,29,0) 72%)}
.story-name{left:600px;top:150px;color:var(--white);font-size:70px;font-weight:800;line-height:96px;letter-spacing:-1px;z-index:2}

/* offer */
.offer{top:1871px;height:543px;background:var(--light)}
.section-title{width:1200px;text-align:center;font-size:33px;font-weight:600;z-index:2}
.offer-title{top:50px}
.offer-card{position:absolute;top:133px;width:320px;text-align:center}
.offer-icon{width:126px;height:126px;margin:0 auto;border-radius:50%;background:var(--dark-2);border:3px solid var(--red);display:flex;align-items:center;justify-content:center}
.offer-card h3{font-size:21px;font-weight:500;margin-top:20px}
.offer-card p{font-size:13px;line-height:27.5px;color:var(--body);margin-top:9px}
.offer-card a{display:inline-block;margin-top:8px;font-size:14px;color:var(--red);text-decoration:underline;font-weight:500}

/* testimonials */
.testimonials{top:2414px;height:673px;background:var(--dark)}
.testi-ghost{left:0;width:1200px;text-align:center;top:38px;font-size:96px}
.testi-title{top:109px;color:var(--white)}
.testi-shadow{left:108px;top:189px;width:492px;height:335px;background:var(--red)}
.testi-video{left:100px;top:181px;width:492px;height:335px;background:linear-gradient(160deg,#7a52c4 0%,#4a4f9a 35%,#2a3352 65%,#1c2230 100%)}
.play-ring{left:214px;top:137px;width:60px;height:60px;border:3px solid var(--white);border-radius:50%;display:flex;align-items:center;justify-content:center}
.dots{left:296px;top:541px;display:flex;gap:11px}
.dots span{width:12px;height:12px;border-radius:50%;background:var(--white)}
.dots span.on{box-shadow:0 0 0 2px var(--dark),0 0 0 3px var(--white)}
.review{position:absolute;left:660px;width:460px}
.avatar{position:absolute;left:0;top:0;width:90px;height:90px;border-radius:50%;background:radial-gradient(circle at 50% 40%,#c9a58a 0%,#8a7262 45%,#e8e8e8 75%);border:3px solid var(--white)}
.quote{position:absolute;left:24px;top:72px;color:var(--red);font-size:40px;font-weight:700;line-height:1}
.review h4{position:absolute;left:109px;top:-8px;color:var(--white);font-size:14px;font-weight:600;white-space:nowrap}
.review h4 span{font-weight:400;font-size:12px;margin-left:6px;padding-left:8px;border-left:1px solid var(--white)}
.review p{position:absolute;left:109px;top:20px;width:340px;color:var(--white);font-size:13px;line-height:25px}

/* gallery */
.gallery{top:3087px;height:720px;background:var(--white)}
.gallery-title{top:46px}
.gallery-item{position:absolute;width:238px;height:230px}
.gallery-btn{left:530px;top:634px;width:140px;height:35px}

/* contact */
.contact{top:3806px;height:941px;background:var(--dark)}
.contact-title{left:114px;top:148px;color:var(--white);font-size:34px;font-weight:400}
.info{position:absolute;left:111px;display:flex;align-items:center;gap:20px;color:var(--white)}
.info-ico{width:44px;height:44px;border-radius:50%;background:var(--red);display:flex;align-items:center;justify-content:center;flex:none}
.info small{display:block;font-size:11px}
.info strong{display:block;font-weight:400;font-size:20px}
.info em{display:block;font-style:normal;font-size:11px}
.follow{left:114px;top:511px;color:var(--white);font-size:31px;font-weight:400}
.socials{left:113px;top:571px;display:flex;gap:8px}
.socials span{width:36px;height:36px;border:1.5px solid var(--white);border-radius:50%}
.form{left:649px;top:158px;width:449px;height:548px;background:var(--white);border-top:5px solid var(--red);padding:24px 27px}
.form h3{font-size:21px;font-weight:500;color:#1d2236}
.field{margin-top:16px;border-bottom:1px solid #bbb;padding-bottom:10px}
.field label{display:block;font-size:14px;font-weight:500;color:#222}
.field span{display:block;font-size:12px;color:#777;margin-top:10px}
.field.msg{height:122px}
.form-btn{left:236px;top:468px;width:186px;height:48px}
.foot-rule{left:100px;top:779px;width:1000px;height:1px;background:rgba(255,255,255,.15)}
.foot-nav{left:0;top:808px;width:1200px;display:flex;justify-content:center;color:var(--white);font-size:14px}
.foot-nav a{color:var(--white);text-decoration:none;padding:0 42px;position:relative}
.foot-nav a+a::before{content:"|";position:absolute;left:-3px}
.copyright{left:0;top:887px;width:1200px;text-align:center;color:var(--white);font-size:14px}
</style>
</head>
<body>

<section class="hero">
  <div class="ph hero-bg" role="img" aria-label="Stage photo of the speaker presenting at a summit, blue and lavender tones"></div>
  <div class="ph hero-photo" role="img" aria-label="Speaker standing on stage with a headset microphone"></div>
  <div class="abs brand">Nikolas Vourtelis</div>
  <nav class="abs nav">
    <a style="left:474px">HOME</a>
    <a style="left:560px">ABOUT US</a>
    <a style="left:678px">OUR SERVICES</a>
    <a style="left:826px">TESTIMONIALS</a>
  </nav>
  <div class="btn nav-cta">Contact Me</div>
  <h1 class="abs hero-title">Public Speaker<br>&amp; Trainer, eCom<br>expert</h1>
  <p class="abs hero-sub">Building &amp; Scaling ecom brands before it was cool (est 2010)</p>
  <p class="abs hero-book">Book A Free Strategy <u>Call Now!</u></p>
  <div class="abs hero-input">Enter Email Here</div>
  <div class="btn hero-btn">Sign Up For My Free Training</div>
  <svg class="abs" style="left:0;top:560px" width="1200" height="113" viewBox="0 0 1200 113">
    <polygon points="0,90 1200,15 1200,40 0,113" fill="var(--red)"/>
    <polygon points="0,113 1200,35 1200,113" fill="#fff"/>
  </svg>
</section>

<section class="about">
  <div class="ph video-frame">
    <div class="video-fill" role="img" aria-label="Video still of an interview between two men seated with a camera between them"></div>
  </div>
  <div class="abs play-red" style="left:330px;top:229px">
    <svg width="22" height="24" viewBox="0 0 22 24"><polygon points="3,1 21,12 3,23" fill="#fff"/></svg>
  </div>
  <h2 class="abs about-title">Hi i'm Nikolas Vourtelis</h2>
  <p class="abs about-text">Lorem ipsum dolor sit amet, consetur adipiscing elit, sed do eiusmod tempor incididunt et dolore magna aliqua. Quis ipsum suspendisse ultces gravida. Risus commodo viverra maecenas accan lacus vel facilisis. Lorem ipsum dolor sit amet, consetur adipiscing elit, sed do eiusmod tempor incididunt et dolore magna aliqua. Quis ipsum suspendisse ultces gravida.</p>
  <div class="btn about-btn">Learn More</div>
</section>

<section class="story">
  <svg class="abs" style="left:0;top:0" width="1200" height="60" viewBox="0 0 1200 60">
    <polygon points="0,0 1200,0 1200,2 0,60" fill="var(--red)"/>
  </svg>
  <div class="abs ghost story-ghost">Story</div>
  <h2 class="abs story-title">My Story</h2>
  <ul class="abs story-list">
    <li>I've spoken to 20 different events around the world up to 3,000 people in size.</li>
    <li>I've sold over 1500 training courses around e-commerce growth.</li>
    <li>I have over 100 testimonials (video &amp; photo) from successful students who bought my training</li>
    <li>I have dozens of video testimonials from respected entrepreneurs that vouch for me and my work</li>
    <li>I have photos with marketing legends with that I shared the stage like Colin Marsh, Thomas Halvorenko, Brent Loy &amp; more</li>
  </ul>
  <div class="btn story-btn">Learn More</div>
  <div class="ph story-photo" role="img" aria-label="Portrait of the speaker on stage wearing a conference lanyard"></div>
  <div class="abs story-name">NIKOLAS<br>VOURTELIS</div>
  <svg class="abs" style="left:0;top:613px" width="1200" height="60" viewBox="0 0 1200 60">
    <polygon points="0,45 1200,0 1200,60 0,60" fill="var(--red)"/>
    <polygon points="0,60 1200,28 1200,60" fill="var(--light)"/>
  </svg>
</section>

<section class="offer">
  <h2 class="abs section-title offer-title">What We Offer</h2>
  <div class="offer-card" style="left:91px">
    <div class="offer-icon">
      <svg width="60" height="56" viewBox="0 0 60 56" fill="none" stroke="#fff" stroke-width="2.5"><rect x="12" y="8" width="40" height="32" rx="2"/><line x1="22" y1="48" x2="42" y2="48"/><line x1="32" y1="40" x2="32" y2="48"/><circle cx="12" cy="12" r="8" fill="#232325"/><path d="M12 7v10M9.5 9.5h4a1.5 1.5 0 010 3h-3a1.5 1.5 0 000 3h4"/><path d="M20 22l10-5v14l-10-5z"/><line x1="36" y1="18" x2="46" y2="18"/><line x1="36" y1="24" x2="46" y2="24"/><line x1="36" y1="30" x2="46" y2="30"/></svg>
    </div>
    <h3>Paid ads</h3>
    <p>Lorem ipsum dolor sit amet, ktur adipiscing elit, sed do eiusmod tempor iidure et dolore magna aliqua. Quis ipm suspendisse ultces gravida. Risus commodo</p>
    <a>LEARN MORE</a>
  </div>
  <div class="offer-card" style="left:441px">
    <div class="offer-icon">
      <svg width="60" height="56" viewBox="0 0 60 56" fill="none" stroke="#fff" stroke-width="2.5"><circle cx="16" cy="10" r="5"/><circle cx="44" cy="10" r="5"/><rect x="22" y="4" width="16" height="12"/><path d="M8 30v-8a6 6 0 0112 0v8M40 30v-8a6 6 0 0112 0v8"/><line x1="6" y1="30" x2="54" y2="30"/><line x1="30" y1="30" x2="30" y2="50"/><path d="M10 30v20M50 30v20M22 50h16"/></svg>
    </div>
    <h3>Consulting</h3>
    <p>Lorem ipsum dolor sit amet, ktur adipiscing elit, sed do eiusmod tempor iidure et dolore magna aliqua. Quis ipm suspendisse ultces gravida. Risus commodo</p>
    <a>LEARN MORE</a>
  </div>
  <div class="offer-card" style="left:789px">
    <div class="offer-icon">
      <svg width="60" height="56" viewBox="0 0 60 56" fill="none" stroke="#fff" stroke-width="2.5"><rect x="20" y="4" width="34" height="26"/><path d="M26 22l6-6 5 4 10-9"/><circle cx="11" cy="12" r="5"/><path d="M5 34v-10a6 6 0 0112 0l6-4M11 34v18M36 30l-6 22M38 30l6 22"/></svg>
    </div>
    <h3>Training</h3>
    <p>Lorem ipsum dolor sit amet, ktur adipiscing elit, sed do eiusmod tempor iidure et dolore magna aliqua. Quis ipm suspendisse ultces gravida. Risus commodo</p>
    <a>LEARN MORE</a>
  </div>
</section>

<section class="testimonials">
  <svg class="abs" style="left:0;top:0" width="1200" height="60" viewBox="0 0 1200 60">
    <polygon points="0,0 1200,0 1200,30 0,60" fill="var(--red)"/>
    <polygon points="0,0 1200,0 1200,12 0,5" fill="var(--light)"/>
  </svg>
  <div class="abs ghost testi-ghost">Testimonials</div>
  <h2 class="abs section-title testi-title">Our Testimonials</h2>
  <div class="ph testi-shadow"></div>
  <div class="ph testi-video" role="img" aria-label="Video still of a panel of four speakers seated on stage">
    <div class="abs play-ring">
      <svg width="20" height="22" viewBox="0 0 20 22"><polygon points="3,1 19,11 3,21" fill="#fff"/></svg>
    </div>
  </div>
  <div class="abs dots"><span class="on"></span><span></span><span></span><span></span></div>

  <div class="review" style="top:180px">
    <div class="avatar" role="img" aria-label="Client portrait"></div><div class="quote">”</div>
    <h4>JOHN SMITH<span>John Smith</span></h4>
    <p>Lorem ipsum dolor sit amet, ktur adipiscing elit, sed do eiusmod tempor iidure et dolore magna aliqua.</p>
  </div>
  <div class="review" style="top:320px">
    <div class="avatar" role="img" aria-label="Client portrait"></div><div class="quote">”</div>
    <h4>JOHN SMITH<span>John Smith</span></h4>
    <p>Lorem ipsum dolor sit amet, ktur adipiscing elit, sed do eiusmod tempor iidure et dolore magna aliqua.</p>
  </div>
  <div class="review" style="top:460px">
    <div class="avatar" role="img" aria-label="Client portrait"></div><div class="quote">”</div>
    <h4>JOHN SMITH<span>John Smith</span></h4>
    <p>Lorem ipsum dolor sit amet, ktur adipiscing elit, sed do eiusmod tempor iidure et dolore magna aliqua.</p>
  </div>
  <svg class="abs" style="left:0;top:613px" width="1200" height="60" viewBox="0 0 1200 60">
    <polygon points="0,60 1200,0 1200,60" fill="var(--red)"/>
    <polygon points="0,60 1200,55 1200,60" fill="#fff"/>
  </svg>
</section>

<section class="gallery">
  <h2 class="abs section-title gallery-title">Our Gallery</h2>
  <div class="gallery-item" style="left:100px;top:122px;background:linear-gradient(160deg,#d8cfc4 0%,#8d7e70 50%,#2f2b2a 100%)" role="img" aria-label="Event photo of two men in suits"></div>
  <div class="gallery-item" style="left:354px;top:122px;background:linear-gradient(180deg,#f4f4f4 0%,#c3c6cc 45%,#4a5060 100%)" role="img" aria-label="Interview set photo"></div>
  <div class="gallery-item" style="left:608px;top:122px;background:linear-gradient(160deg,#d6b894 0%,#a48462 50%,#4a3a2c 100%)" role="img" aria-label="Portrait at a conference venue"></div>
  <div class="gallery-item" style="left:862px;top:122px;background:linear-gradient(160deg,#6a7a94 0%,#3b4456 50%,#2a2624 100%)" role="img" aria-label="Photo of two entrepreneurs at an evening event"></div>
  <div class="gallery-item" style="left:100px;top:371px;background:linear-gradient(160deg,#c8d2e0 0%,#7f8ba0 50%,#2e3240 100%)" role="img" aria-label="Speaker in front of a summit banner"></div>
  <div class="gallery-item" style="left:354px;top:371px;background:linear-gradient(160deg,#e6e2dc 0%,#a99482 50%,#3c3632 100%)" role="img" aria-label="Photo of two men side by side"></div>
  <div class="gallery-item" style="left:608px;top:371px;background:linear-gradient(160deg,#b48a62 0%,#7a5a40 50%,#2c2420 100%)" role="img" aria-label="Photo with a marketing guest at a dinner"></div>
  <div class="gallery-item" style="left:862px;top:371px;background:linear-gradient(160deg,#c9a67e 0%,#8c7058 50%,#2b2a2c 100%)" role="img" aria-label="Photo with a guest in a hotel lobby"></div>
  <div class="btn gallery-btn">View All</div>
</section>

<section class="contact">
  <svg class="abs" style="left:0;top:0" width="1200" height="100" viewBox="0 0 1200 100">
    <polygon points="0,0 1200,0 0,85" fill="#fff"/>
    <polygon points="0,80 1200,0 1200,8 0,96" fill="var(--red)"/>
  </svg>
  <h2 class="abs contact-title">Contact Us</h2>
  <div class="info" style="top:239px">
    <div class="info-ico"><svg width="18" height="22" viewBox="0 0 18 22"><path d="M9 1a7 7 0 017 7c0 5-7 13-7 13S2 13 2 8a7 7 0 017-7z" fill="#fff"/><circle cx="9" cy="8" r="2.6" fill="#e3173d"/></svg></div>
    <div><small>Location</small><strong>48 Harbor Lane Westfield, US 20417</strong></div>
  </div>
  <div class="info" style="top:330px">
    <div class="info-ico"><svg width="20" height="20" viewBox="0 0 20 20"><path d="M5 2l3 4-2 2c1 2.5 3 4.5 5.5 5.5l2-2 4 3-2 3C9 17 3 11 2 4z" fill="#fff"/></svg></div>
    <div><strong>Call Us At (555) 014-2290</strong><em>Or&nbsp; Click Here to Request An Online Appointment</em></div>
  </div>
  <div class="info" style="top:424px">
    <div class="info-ico"><svg width="20" height="16" viewBox="0 0 20 16"><rect x="1" y="2" width="18" height="12" rx="1.5" fill="#fff"/><path d="M2 3l8 6 8-6" fill="none" stroke="#e3173d" stroke-width="1.6"/></svg></div>
    <div><small>Email Us</small><strong>hello@vourtelisgrowth.co</strong></div>
  </div>
  <h3 class="abs follow">Follow On</h3>
  <div class="abs socials" aria-label="Social profiles"><span></span><span></span><span></span><span></span></div>

  <form class="abs form">
    <h3>Send Us Message</h3>
    <div class="field"><label>Name</label><span>John Smith</span></div>
    <div class="field"><label>Email</label><span>JohnSmith@gmail.com</span></div>
    <div class="field"><label>Phone Number</label><span>+1</span></div>
    <div class="field msg"><label>Message</label><span>Type Your Message</span></div>
    <div class="btn form-btn">Submith Now</div>
  </form>

  <div class="abs foot-rule"></div>
  <nav class="abs foot-nav"><a>HOME</a><a>ABOUT US</a><a>OUR SERVICES</a><a>TESTIMONIALS</a><a>CONTACT US</a></nav>
  <p class="abs copyright">©Copyright 2023 Nikolas Vourtelis. All Rights Reserved.</p>
</section>

</body>
</html>
```